KT Appraisals BV business cards (a financial services company)

I am looking for a business card design that stands out in the financial advisory field of business & intellectual property valuation. The business card design should be conservative, yet different. Address details have changed since the attached business card. New address is:

Dorpelstraat 27
4817 KM Leiden
The Netherlands

Telephone number remains the same.

```html
<!DOCTYPE html>
<html lang="en">
<head>
<meta charset="utf-8">
<title>KT Appraisals BV – Business Card</title>
<link rel="stylesheet" href="https://fonts.googleapis.com/css2?family=Roboto+Condensed:wght@400;700&display=swap">
<style>
  :root {
    --page-bg: #e4e4e4;
    --card-white: #ffffff;
    --panel-grey: #7c7f7b;
    --stripe-mid: #b4b4b4;
    --stripe-light: #d6d6d6;
    --rule: #8a8a8a;
    --ink-light: #ffffff;
    --ink-muted: #8b8b8b;
    --ink-brand: #6f6f6f;
    --icon: #262626;
  }
  * { margin: 0; padding: 0; box-sizing: border-box; }
  html, body {
    width: 1200px; height: 1200px; overflow: hidden;
    background: var(--page-bg);
    font-family: "Roboto Condensed", Arial, sans-serif;
  }
  .card {
    position: absolute; left: 66px; top: 272px;
    width: 1068px; height: 656px;
    background: var(--card-white);
    box-shadow: 0 14px 30px rgba(0,0,0,0.25);
    overflow: hidden;
  }
  .card-shapes { position: absolute; inset: 0; }
  .brand {
    position: absolute; left: 0; width: 472px; top: 266px;
    text-align: center;
  }
  .brand-name {
    display: inline-flex; align-items: center; gap: 14px;
    font-size: 40px; font-weight: 400; letter-spacing: 1px;
    color: var(--ink-brand);
  }
  .brand-mark { width: 22px; height: 22px; background: var(--ink-brand); }
  .brand-tagline {
    margin-top: 44px;
    font-size: 27px; line-height: 35px; color: var(--ink-muted);
    letter-spacing: 0.3px;
  }
  .person { position: absolute; left: 484px; top: 86px; color: var(--ink-light); }
  .person-name { font-size: 41px; font-weight: 700; letter-spacing: 0.3px; }
  .person-credentials { font-size: 31px; font-weight: 400; }
  .person-title { margin: 4px 0 0 24px; font-size: 32px; letter-spacing: 0.3px; }
  .contact { position: absolute; left: 570px; color: var(--ink-light); font-size: 27px; }
  .contact-row { display: flex; align-items: flex-start; gap: 14px; line-height: 35px; }
  .contact-row svg { flex: none; width: 26px; height: 26px; margin-top: 4px; fill: var(--icon); }
  .contact-address { top: 258px; }
  .contact-phone { top: 410px; }
  .contact-email { top: 460px; }
  .contact-web { top: 510px; }
</style>
</head>
<body>
  <div class="card">
    <svg class="card-shapes" viewBox="0 0 1068 656" width="1068" height="656" aria-hidden="true">
      <polygon points="285,0 1068,0 1068,656 376,656 515,392" fill="var(--stripe-light)"/>
      <polygon points="302,0 1068,0 1068,656 393,656 532,392" fill="var(--stripe-mid)"/>
      <polygon points="319,0 1068,0 1068,656 410,656 549,392" fill="var(--panel-grey)"/>
      <g stroke="var(--rule)" stroke-width="1">
        <line x1="0" y1="608" x2="1068" y2="608"/>
        <line x1="0" y1="614" x2="1068" y2="614"/>
        <line x1="0" y1="620" x2="1068" y2="620"/>
        <line x1="0" y1="626" x2="1068" y2="626"/>
        <line x1="0" y1="632" x2="1068" y2="632"/>
        <line x1="0" y1="638" x2="1068" y2="638"/>
        <line x1="0" y1="644" x2="1068" y2="644"/>
        <line x1="0" y1="650" x2="1068" y2="650"/>
      </g>
    </svg>

    <div class="brand">
      <div class="brand-name"><span class="brand-mark"></span>KT APPRAISALS</div>
      <p class="brand-tagline">BUSINESS &amp; INTELLECTUAL<br>PROPERTY VALUATIONS</p>
    </div>

    <div class="person">
      <div><span class="person-name">MARTIN DEKKER,</span> <span class="person-credentials">CFA, ASA, RV</span></div>
      <div class="person-title">MANAGING DIRECTOR</div>
    </div>

    <div class="contact contact-address">
      <div class="contact-row">
        <svg viewBox="0 0 24 24"><path d="M12 2a7 7 0 0 0-7 7c0 5 7 13 7 13s7-8 7-13a7 7 0 0 0-7-7zm0 9.5A2.5 2.5 0 1 1 12 6.5a2.5 2.5 0 0 1 0 5z"/></svg>
        <address style="font-style:normal">Dorpelstraat 27<br>4817 KM Leiden<br>The Netherlands</address>
      </div>
    </div>
    <div class="contact contact-phone">
      <div class="contact-row">
        <svg viewBox="0 0 24 24"><path d="M6.6 10.8a15 15 0 0 0 6.6 6.6l2.2-2.2a1 1 0 0 1 1-.25 11.4 11.4 0 0 0 3.6.57 1 1 0 0 1 1 1V20a1 1 0 0 1-1 1A17 17 0 0 1 3 4a1 1 0 0 1 1-1h3.5a1 1 0 0 1 1 1c0 1.25.2 2.45.57 3.57a1 1 0 0 1-.25 1z"/></svg>
        <span>+31 (0)70 384 1726</span>
      </div>
    </div>
    <div class="contact contact-email">
      <div class="contact-row">
        <svg viewBox="0 0 24 24"><path d="M2 5h20v14H2zm2 2v.4l8 5.2 8-5.2V7zm0 2.8V17h16V9.8l-8 5.2z"/></svg>
        <span>mdekker@ktappraisals.com</span>
      </div>
    </div>
    <div class="contact contact-web">
      <div class="contact-row">
        <svg viewBox="0 0 24 24"><path d="M12 2a10 10 0 1 0 0 20 10 10 0 0 0 0-20zm6.9 6h-2.9a15 15 0 0 0-1.4-3.6A8 8 0 0 1 18.9 8zM12 4a13 13 0 0 1 1.9 4h-3.8A13 13 0 0 1 12 4zM4.3 14a8 8 0 0 1 0-4h3.4a16 16 0 0 0 0 4zm.8 2h2.9a15 15 0 0 0 1.4 3.6A8 8 0 0 1 5.1 16zM8 8H5.1a8 8 0 0 1 4.3-3.6A15 15 0 0 0 8 8zm4 12a13 13 0 0 1-1.9-4h3.8A13 13 0 0 1 12 20zm2.3-6H9.7a14 14 0 0 1 0-4h4.6a14 14 0 0 1 0 4zm.3 5.6a15 15 0 0 0 1.4-3.6h2.9a8 8 0 0 1-4.3 3.6zm1.7-5.6a16 16 0 0 0 0-4h3.4a8 8 0 0 1 0 4z"/></svg>
        <span>www.ktappraisals.com</span>
      </div>
    </div>
  </div>
</body>
</html>
```